Stationery Design Project

We are a packaging machinery manufacturer that mainly serve the food industry.
We now require a full set of stationary including name card, envelop, letter paper, and etc. to match our company image. The logo has been awarded in a previous contest which is attached here.
Updates
Project Deadline Extended
Reason: We have extended the deadline. We have adjusted the deadline before launch to avoid confusion but it turns out the new date wasn't implemented by the system. All designers please feel free to submit your design. Thank you!
Target Market(s)
B2B customer, including decision maker in food factories, chemical factories, etc.
Industry/Entity Type
Industry
Colors
Designer to choose colors to be used in the design.
Look and feel
Each slider illustrates characteristics of the customer's brand and the style your logo design should communicate.

```html
<!DOCTYPE html>
<html lang="en">
<head>
<meta charset="utf-8">
<title>VORTAN Business Card</title>
<link href="https://fonts.googleapis.com/css2?family=Open+Sans:wght@400;600;700&display=swap" rel="stylesheet">
<style>
  :root {
    --brand-green: #046b3a;
    --brand-grey: #8a9096;
    --text-grey: #7d8388;
    --card-white: #ffffff;
    --backdrop: #c6c6c6;
  }
  * { margin: 0; padding: 0; box-sizing: border-box; }
  html, body {
    width: 1200px;
    height: 900px;
    overflow: hidden;
    background: var(--backdrop);
    font-family: "Open Sans", Arial, sans-serif;
  }
  .card {
    position: absolute;
    width: 616px;
    height: 352px;
    background: var(--card-white);
  }
  .card--front { left: 288px; top: 81px; }
  .card--back { left: 288px; top: 467px; overflow: hidden; }

  .brand-name {
    position: absolute;
    left: 49px;
    top: 44px;
    display: flex;
    align-items: center;
    gap: 8px;
    font-size: 40px;
    font-weight: 700;
    line-height: 1;
    letter-spacing: 1px;
    color: var(--brand-green);
  }
  .brand-name__square {
    width: 28px;
    height: 28px;
    background: var(--brand-green);
  }

  .holder-name {
    position: absolute;
    left: 49px;
    top: 190px;
    font-size: 24px;
    font-weight: 600;
    color: var(--brand-green);
  }
  .holder-role {
    position: absolute;
    left: 49px;
    top: 220px;
    font-size: 15px;
    letter-spacing: 0.5px;
    color: var(--text-grey);
  }

  .contact {
    position: absolute;
    font-size: 14.5px;
    line-height: 19px;
    letter-spacing: 0.5px;
    color: var(--text-grey);
  }
  .contact--personal { left: 49px; top: 278px; }
  .contact--company { left: 302px; top: 259px; }
  .contact__label { color: var(--brand-green); }
  .contact__company-name { color: var(--brand-green); font-weight: 600; letter-spacing: 0; }

  .brand-field {
    position: absolute;
    left: 0;
    top: 0;
    width: 352px;
    height: 352px;
    background: var(--brand-green);
  }
  .website {
    position: absolute;
    left: 413px;
    top: 164px;
    font-size: 16px;
    font-weight: 700;
    color: var(--brand-green);
  }
</style>
</head>
<body>
  <section class="card card--front">
    <div class="brand-name"><span class="brand-name__square"></span>VORTAN</div>
    <div class="holder-name">Your Name</div>
    <div class="holder-role">Managing Director</div>
    <div class="contact contact--personal">
      <div><span class="contact__label">MOBILE:</span> 123 456 7890</div>
      <div><span class="contact__label">EMAIL:</span> name@vortan.com</div>
    </div>
    <div class="contact contact--company">
      <div class="contact__company-name">VORTAN Pakaging Technology</div>
      <div>Your Office, City, XXXXX Country</div>
      <div><span class="contact__label">TEL:</span> 123 456 7890&nbsp;&nbsp;<span class="contact__label">FAX:</span> 123 456 7890</div>
    </div>
  </section>

  <section class="card card--back">
    <div class="brand-field" role="img" aria-label="Large brand symbol area in green and grey"></div>
    <div class="website">www.vortan.com</div>
  </section>
</body>
</html>
```